IT Network Consultancy - Business Card

t4 linkways is a IT network consultancy based in London. We're looking for a smart, modern and professional business card design. Our website is here: www.t4linkways.co.uk

Key things that should be included on the card (with examples):

Company Logo
Name
Position / Job Title: Network Consultant
Mobile Phone Number: +44 (0) 7700 900418
Land Line: +44 (0) 1632 960274
Email Address: name@t4linkways.co.uk
Web Site URL: www.t4linkways.co.uk

Target Market(s)

Large enterprise / global companies / corporates

Industry/Entity Type

Business

Requirements
Must have
• Incorporate our logo - which is attached to the project. They are in AI format (can be opened in Inkscape).

The design should be double sided and fit on a UK standard 85mm × 55mm card and be in a format that retains the quality when printed.
Nice to have
• The project does not have to conform to the colour of our website but this should give you inspiration of the style we like.
Should not have
• Bright colours. Pictures are not necessary.

```html
<!DOCTYPE html>
<html lang="en">
<head>
<meta charset="utf-8">
<title>t4 linkways – Business Card</title>
<link rel="stylesheet" href="https://fonts.googleapis.com/css2?family=Questrial&display=swap">
<style>
  :root {
    --band-dark: #121c21;
    --rule-light: #b9c4cb;
    --panel-base: #929fa8;
    --panel-deep: #87949d;
    --panel-glow: #d3dbe0;
    --text-white: #ffffff;
    --text-slate: #4a535a;
    --text-logo: #c8d0d5;
    --text-url: #d4dbe0;
  }
  * { margin: 0; padding: 0; box-sizing: border-box; }
  html, body {
    width: 1200px;
    height: 777px;
    overflow: hidden;
    background: #ffffff;
  }
  .card {
    position: relative;
    width: 1200px;
    height: 777px;
    font-family: "Questrial", "Century Gothic", sans-serif;
    overflow: hidden;
    background: var(--band-dark);
  }
  .card__header {
    position: absolute;
    left: 0; top: 0;
    width: 100%;
    height: 125px;
    background: var(--band-dark);
  }
  .brand-name {
    position: absolute;
    left: 26px;
    top: 22px;
    font-size: 68px;
    line-height: 1;
    letter-spacing: 3px;
    color: var(--text-logo);
    text-transform: uppercase;
  }
  .card__panel {
    position: absolute;
    left: 0; top: 125px;
    width: 100%;
    height: 590px;
    border-top: 4px solid var(--rule-light);
    border-bottom: 4px solid var(--rule-light);
    background:
      radial-gradient(ellipse 260px 200px at 640px 20px, var(--panel-glow) 0%, rgba(211,219,224,0) 100%),
      linear-gradient(180deg, var(--panel-base) 0%, var(--panel-deep) 100%);
  }
  .person {
    position: absolute;
    left: 0; top: 325px;
    width: 1196px;
    text-align: center;
  }
  .person__name {
    font-size: 50px;
    line-height: 1;
    color: var(--text-white);
    font-weight: 400;
  }
  .person__role {
    margin-top: 12px;
    font-size: 37px;
    line-height: 1;
    color: var(--text-slate);
    padding-right: 10px;
  }
  .contact {
    position: absolute;
    right: 29px;
    top: 524px;
    list-style: none;
    text-align: right;
    color: var(--text-slate);
    font-size: 41px;
    line-height: 51px;
    letter-spacing: 0.6px;
  }
  .card__footer {
    position: absolute;
    left: 0; bottom: 0;
    width: 100%;
    height: 62px;
    background: var(--band-dark);
  }
  .website {
    position: absolute;
    right: 28px;
    bottom: 6px;
    font-size: 45px;
    line-height: 1;
    color: var(--text-url);
  }
</style>
</head>
<body>
  <div class="card">
    <header class="card__header">
      <div class="brand-name">t4 linkways</div>
    </header>

    <section class="card__panel"></section>

    <div class="person">
      <h1 class="person__name">Name Namename</h1>
      <p class="person__role">Network Consultant</p>
    </div>

    <ul class="contact">
      <li class="contact__mobile">Mobile:+44 (0) 7700 900418</li>
      <li class="contact__landline">Land Line: +44 (0) 1632 960274</li>
      <li class="contact__email">Email: name@t4linkways.co.uk</li>
    </ul>

    <footer class="card__footer">
      <div class="website">www.t4linkways.co.uk</div>
    </footer>
  </div>
</body>
</html>
```